14 years in business and its time for a new look and feel brochure and business cards!

We are looking to create a brochure that is professional and eye catching to bring in new commercial business. After14 years in business we have finally redone our logo and it is time to get a brochure completed as well. The logo that should be used is the one that says Inc. We want this new brochure to appeal to corporate property management companies and smaller apartment complexes. We want it to look rich and have the same high quality our work has.

Target Market(s)

property management companies and apartment complexes in the DMV.

Industry/Entity Type

Construction Company

Contact Information for Business Card

Logo
Dovid Rennick
CEO
Mobile 410-555-0137
Office 410-555-0192
Address 3817 Larchmont Lane Suite B Baltimore, MD 21208
Email DR@BrightCoatInc.example

Font styles to use
Sans Serif

Requirements
Must have
• Want the background to be black and silver gradient. Will be printing on high gloss and would like for it to be rich looking.
• brochure will be 8.5x11. open minded in terms of the fold, how it looks best with the design provided will determine that. Can be bi-fold, try-fold or z-fold.
• Content for brochure:About us
• Founded in 2003, The Bright Coat Inc. was the vision of Dovid Rennick, with a commitment to becoming the premier renovator and developer of residential and commercial properties in the DMV. Today, The Bright Coat Inc. is widely respected for their gold standard in quality and efficiency and continues to grow by attracting the highest level of professionals with knowledge and experience in our field.
• The Bright Coat Inc.’s most valuable asset is our team members. The efforts they put forth are the key to meeting our standards and providing all of our valued clients with the highest quality of service. Leading our wonderful team members is a group of management like no other. With years of experience, the power to motivate and the keen eye to ensure top quality, our team of experts focus all of their energy to exceed our client’s expectations.
• Our Mission
• We strive to provide timely delivery, the highest level of quality and value on every project. We offer unsurpassed dedication to maintain our working relationships and consistently deliver the best service to ensure our clients success.
• Property Renovations
• The Bright Coat Inc. has been responsible for coordinating the construction and renovation of many projects, including all parts of a building’s interior and exterior. Well known for attention to details, quality and timely execution, The Bright Coat Inc. has managed and executed more than 4,000 turnovers and over 150 projects in the last 3 years alone.
• Renovations not only improve the appeal and marketability of your property, but also add value. Interior and exterior renovations help make any property more functional, energy-efficient and enable you to keep up with what your market demands. From the smallest change of a door knob to a complete kitchen overhaul, these are the things that make all the difference in your property. We are committed to deliver great value, and we do that by ensuring that our experts are involved in the renovation process, providing input and quality maintenance throughout the entire renovation.
• Services Include
• Painting
• Flooring
• Sub-Flooring
• Crown molding
• Siding & Wood Replacement
• Trim & Carpentry Work
• Punches
• Decks
• Power wash
• Concrete & Paving
• Turnovers including plumbing and electric
• Kitchen overhauls
• We offer first time clients a free apartment paint or punch on us to show you the quality you can always expect!
• Call today to schedule your first-time paint or punch at 410-555-0192.

```html
<!DOCTYPE html>
<html lang="en">
<head>
<meta charset="utf-8">
<title>The Bright Coat Inc. — Business Card</title>
<link rel="stylesheet" href="https://fonts.googleapis.com/css2?family=Exo+2:wght@400;600;800&display=swap">
<style>
  :root {
    --page: #e4e4e4;
    --card-dark: #0c0c0c;
    --card-mid: #2a2a2a;
    --silver: #d9d9d9;
    --silver-soft: #a8a8a8;
    --silver-dim: #8a8a8a;
  }
  * { margin: 0; padding: 0; box-sizing: border-box; }
  html, body {
    width: 1200px; height: 1200px; overflow: hidden;
    background: var(--page);
    font-family: "Exo 2", sans-serif;
  }
  .sheet {
    width: 1200px; height: 1200px;
    display: flex; flex-direction: column;
    align-items: center; justify-content: center; gap: 60px;
  }
  .card {
    position: relative;
    width: 900px; height: 514px;
    background:
      radial-gradient(ellipse 60% 80% at 38% 30%, rgba(255,255,255,0.14), transparent 70%),
      linear-gradient(125deg, var(--card-mid) 0%, var(--card-dark) 45%, #1d1d1d 70%, var(--card-dark) 100%);
    box-shadow: 0 14px 30px rgba(0,0,0,0.25);
    color: var(--silver);
    overflow: hidden;
  }

  /* Back: contact details */
  .card--back .contact {
    position: absolute; left: 470px; top: 110px;
    width: 360px;
  }
  .contact__name {
    font-weight: 800; font-size: 40px; letter-spacing: 2px;
    color: #f2f2f2; text-transform: uppercase;
  }
  .contact__role {
    font-size: 14px; letter-spacing: 3px; color: var(--silver-dim);
    text-transform: uppercase; margin-top: 4px;
  }
  .contact__icons { display: flex; gap: 14px; margin-top: 30px; }
  .contact__icons svg { width: 30px; height: 30px; }
  .contact__lines {
    list-style: none; margin-top: 18px;
    font-size: 22px; line-height: 1.5; color: var(--silver);
  }

  /* Front: brand */
  .card--front .brand {
    position: absolute; left: 0; right: 0; top: 170px;
    display: flex; align-items: center; justify-content: center; gap: 22px;
  }
  .brand__mark {
    width: 70px; height: 70px; border-radius: 50%;
    background: var(--silver-soft);
  }
  .brand__name {
    font-weight: 800; font-size: 60px; letter-spacing: 1px;
    color: var(--silver); text-transform: uppercase;
  }
  .card--front .web {
    position: absolute; left: 0; right: 0; top: 300px;
    text-align: center;
    font-size: 24px; letter-spacing: 9px; color: var(--silver-soft);
    text-transform: uppercase;
  }
</style>
</head>
<body>
<main class="sheet">
  <section class="card card--back" aria-label="Business card back">
    <div class="contact">
      <p class="contact__name">Your Name</p>
      <p class="contact__role">Designation</p>
      <div class="contact__icons">
        <svg viewBox="0 0 30 30" aria-label="Address"><circle cx="15" cy="15" r="13" fill="none" stroke="#d9d9d9" stroke-width="1.6"/><path d="M15 8a4.5 4.5 0 0 0-4.5 4.5c0 3.4 4.5 8.5 4.5 8.5s4.5-5.1 4.5-8.5A4.5 4.5 0 0 0 15 8z" fill="none" stroke="#d9d9d9" stroke-width="1.5"/><circle cx="15" cy="12.5" r="1.5" fill="#d9d9d9"/></svg>
        <svg viewBox="0 0 30 30" aria-label="Phone"><circle cx="15" cy="15" r="13" fill="none" stroke="#d9d9d9" stroke-width="1.6"/><path d="M11 9l2.5 0 1 3-1.5 1.2a7 7 0 0 0 3.3 3.3l1.2-1.5 3 1v2.5c0 .8-.7 1.5-1.5 1.5A9.5 9.5 0 0 1 9.5 10.5C9.5 9.7 10.2 9 11 9z" fill="#d9d9d9"/></svg>
        <svg viewBox="0 0 30 30" aria-label="Email"><circle cx="15" cy="15" r="13" fill="none" stroke="#d9d9d9" stroke-width="1.6"/><rect x="8.5" y="10.5" width="13" height="9" fill="none" stroke="#d9d9d9" stroke-width="1.5"/><path d="M8.5 10.5l6.5 5 6.5-5" fill="none" stroke="#d9d9d9" stroke-width="1.5"/></svg>
        <svg viewBox="0 0 30 30" aria-label="Website"><circle cx="15" cy="15" r="13" fill="none" stroke="#d9d9d9" stroke-width="1.6"/><circle cx="15" cy="15" r="6.5" fill="none" stroke="#d9d9d9" stroke-width="1.4"/><ellipse cx="15" cy="15" rx="2.8" ry="6.5" fill="none" stroke="#d9d9d9" stroke-width="1.2"/><path d="M8.5 15h13" stroke="#d9d9d9" stroke-width="1.2"/></svg>
      </div>
      <ul class="contact__lines">
        <li>Address Goes Here</li>
        <li>410-555-0192</li>
        <li>info@brightcoatinc.example</li>
        <li>www.brightcoatinc.example</li>
      </ul>
    </div>
  </section>

  <section class="card card--front" aria-label="Business card front">
    <div class="brand">
      <span class="brand__mark" aria-hidden="true"></span>
      <span class="brand__name">The Bright Coat Inc</span>
    </div>
    <p class="web">www.brightcoatinc.example</p>
  </section>
</main>
</body>
</html>
```